Emergency Vehicle Installer and Security Firm Needs a Business Card

Our company "Corvalta" need a business card for our Emergency Vehicle Equipment Installation and Infrastructure Security Business. We are contract designers, manufacturers and installers for Emergency Vehicle Fleets. This includes installation of Emergency Lights, Sirens, Vehicle Graphics and Radio Communications. We also supply this products to an international market. We also do consultant, and installation of high level security access, alarm and surveillance equipment for medium to large size businesses.

The design should represent a level of trust in our professionalism and expertise. It should visually display our ongoing relationship with the emergency services, but not overtake our commitment to high level security options.

Target Market(s)

Emergency Services and Businesses requiring high level security

Industry/Entity Type

Business

Contact Information for Business Card

*note complete details will be given to the winning designer for revising. The name "Mark Pelling will be used to fill in name".

Mark Pelling
Managing Director
Corvalta NZ Limited
Phone: +64 027 846 20193
Email: mark.pelling@corvalta-example.co.nz

Requirements
Must have
• Card must be in black. Using our logo on the top as supplied. Designers should try having the reverse side as a blurred image of police lights (red and blue) with our logo in greyscale in the centre (this is not particularly a requirement, but feel free to play around with this option).
Nice to have
• A card design that looks good when spot UV printed. A clean compact and graphic design. A grey scale feel on the front (excluding logo, but you can play around with that idea). Rounded smooth text.
Should not have
• Will update this section as designs come through - feel free to submit what you feel would look good.

```html
<!DOCTYPE html>
<html lang="en">
<head>
<meta charset="utf-8">
<title>Corvalta Business Card</title>
<link href="https://fonts.googleapis.com/css2?family=Open+Sans:wght@400;600;800&display=swap" rel="stylesheet">
<style>
  :root {
    --canvas-bg: #e9e7e3;
    --card-black: #0b0b0b;
    --ink-white: #f4f4f4;
    --ink-grey: #c9c9c9;
    --accent-red: #e4262f;
    --light-red: #d4262e;
    --light-magenta: #c02a9a;
    --light-violet: #7a45c8;
    --light-blue: #3a62d8;
  }
  * { margin: 0; padding: 0; box-sizing: border-box; }
  html, body {
    width: 1200px; height: 780px; overflow: hidden;
    background: var(--canvas-bg);
    font-family: "Open Sans", Arial, sans-serif;
  }
  .canvas {
    position: relative; width: 1200px; height: 780px;
    display: flex; align-items: center; justify-content: center; gap: 40px;
  }
  .card {
    position: relative; width: 540px; height: 310px;
    border-radius: 6px; overflow: hidden;
    box-shadow: 0 10px 30px rgba(0,0,0,.25);
  }
  .card-front { background: var(--card-black); }
  .wordmark {
    font-family: "Open Sans", Arial, sans-serif;
    font-weight: 800; color: var(--ink-white);
    letter-spacing: 1px; line-height: 1;
  }
  .card-front .wordmark {
    position: absolute; left: 36px; bottom: 70px; font-size: 50px;
  }
  .contact-block {
    position: absolute; right: 34px; top: 40px; width: 230px;
    color: var(--ink-white);
  }
  .company-name { font-size: 17px; font-weight: 600; margin-bottom: 26px; }
  .person-name { font-size: 17px; font-weight: 800; color: var(--accent-red); }
  .person-title { font-size: 13px; color: var(--ink-grey); margin-bottom: 20px; }
  .contact-line {
    display: flex; align-items: center; gap: 8px;
    font-size: 11.5px; color: var(--ink-grey); margin-bottom: 6px;
    white-space: nowrap;
  }
  .contact-icon {
    width: 14px; height: 14px; flex: none; background: var(--accent-red);
    border-radius: 2px; display: flex; align-items: center; justify-content: center;
  }
  .card-back {
    background: var(--card-black);
  }
  .police-lights {
    position: absolute; inset: 0;
    background:
      radial-gradient(ellipse 45% 55% at 38% 25%, var(--light-red), transparent 70%),
      radial-gradient(ellipse 55% 55% at 55% 50%, var(--light-magenta), transparent 75%),
      radial-gradient(ellipse 60% 60% at 65% 85%, var(--light-blue), transparent 80%),
      radial-gradient(ellipse 40% 40% at 60% 70%, var(--light-violet), transparent 80%),
      var(--card-black);
  }
  .card-back .wordmark {
    position: absolute; left: 0; right: 0; top: 50%;
    transform: translateY(-50%); text-align: center; font-size: 54px;
  }
</style>
</head>
<body>
<main class="canvas">
  <section class="card card-front" aria-label="Card front">
    <div class="wordmark">CORVALTA</div>
    <div class="contact-block">
      <p class="company-name">Corvalta NZ Limited</p>
      <p class="person-name">Mark Pelling</p>
      <p class="person-title">Managing Director</p>
      <p class="contact-line">
        <span class="contact-icon">
          <svg width="10" height="10" viewBox="0 0 10 10"><path d="M2 1 L4 3 L3 4 Q4 6 6 7 L7 6 L9 8 L8 9 Q3 9 1 2 Z" fill="#fff"/></svg>
        </span>
        +64 027 846 20193
      </p>
      <p class="contact-line">
        <span class="contact-icon">
          <svg width="10" height="10" viewBox="0 0 10 10"><rect x="1" y="2.5" width="8" height="5.5" fill="none" stroke="#fff" stroke-width="1"/><path d="M1 2.5 L5 6 L9 2.5" fill="none" stroke="#fff" stroke-width="1"/></svg>
        </span>
        mark.pelling@corvalta-example.co.nz
      </p>
    </div>
  </section>
  <section class="card card-back" aria-label="Card back">
    <div class="police-lights" role="img" aria-label="Blurred red and blue emergency vehicle lights"></div>
    <div class="wordmark">CORVALTA</div>
  </section>
</main>
</body>
</html>
```